Travel Company is looking for a STAND OUT Business Card

I need a unique Business Card that will truly stand out. Nothing too busy. Simple is good, right? Not looking for a standard design either. No cookie cutter layout. We are a Travel Company that works more with Companies than Travelers. I had an idea to focus and emphasis on the 2 logo a bit more. This is not necessary, however thought it would look interesting. I am just looking for something interesting and a bit different. Does't have to completely off the wall crazy, just not your run of the mill business card.

Target Market(s)

Hoteliers, Resort Management, Call Centers, Executives, Travelers, Families, Businesses

Industry/Entity Type

Hospitality

Contact Information for Business Card

President/CEO - Marcus T Bellamy (title not necessary if design doesn't allow for it)
contact - (407) 555-0186
email - mbellamy@wayfarenow.example
address - 4812 Quillmore Ave #164
Orlando, FL 32804
website - www.wayfarenow.example

Font styles to use
Serif
Other font styles liked:
• Avenir Next LT Pro BOLD

Requirements
Must have
• simple look and design. Unique design
Nice to have
• I attached the 2 logo separate from the main logo. This can be used separately from the Main Logo, together with the main logo or as main logo. I included the logo font. Use it or not, designers choice.
Should not have
• cookie cutter design. Little use of red other than the logo

```html
<!DOCTYPE html>
<html lang="en">
<head>
<meta charset="utf-8">
<title>wayfarenow – Business Card</title>
<link rel="stylesheet" href="https://fonts.googleapis.com/css2?family=Nunito+Sans:wght@700;800;900&display=swap">
<style>
  :root {
    --backdrop: #9098c2;
    --card: #333333;
    --ink-light: #ffffff;
    --ink-dark: #111111;
    --accent: #e8333a;
  }
  * { margin: 0; padding: 0; box-sizing: border-box; }
  html, body { width: 1200px; height: 1200px; overflow: hidden; }
  body {
    background: var(--backdrop);
    font-family: "Nunito Sans", "Avenir Next", sans-serif;
    position: relative;
  }
  .card { position: absolute; background: var(--card); overflow: hidden; }

  /* Front */
  .card-front { left: 138px; top: 69px; width: 397px; height: 660px; }
  .brand {
    display: flex; align-items: center; gap: 8px;
    color: var(--ink-light); font-weight: 900; letter-spacing: -0.5px;
  }
  .card-front .brand {
    position: absolute; top: 80px; left: 0; width: 100%;
    justify-content: center; font-size: 32px;
  }
  .brand-dot { width: 14px; height: 14px; border-radius: 50%; background: var(--accent); flex: none; }
  .name-band { position: absolute; left: 0; top: 229px; width: 397px; height: 130px; }
  .holder-name {
    position: absolute; left: 30px; top: 265px;
    font-size: 32px; font-weight: 900; color: var(--ink-dark); letter-spacing: -0.3px;
    white-space: nowrap;
  }
  .contact-list { position: absolute; left: 36px; top: 432px; right: 12px; list-style: none; }
  .contact-item {
    display: flex; align-items: flex-start; gap: 22px;
    color: var(--ink-light); font-size: 18.5px; font-weight: 800; line-height: 1.1;
    margin-bottom: 18px; white-space: nowrap;
  }
  .contact-icon { width: 20px; height: 20px; flex: none; margin-top: 1px; }

  /* Back */
  .card-back { left: 460px; top: 780px; width: 600px; height: 360px; }
  .card-back .brand {
    position: absolute; top: 140px; left: 0; width: 100%;
    justify-content: center; font-size: 58px; gap: 14px;
  }
  .card-back .brand-dot { width: 24px; height: 24px; }
  .back-url {
    position: absolute; bottom: 38px; left: 0; width: 100%; text-align: center;
    color: var(--ink-light); font-size: 20px; font-weight: 800; letter-spacing: 0.5px;
  }
</style>
</head>
<body>

<section class="card card-front">
  <div class="brand"><span class="brand-dot"></span>wayfarenow</div>

  <svg class="name-band" viewBox="0 0 397 130" aria-hidden="true">
    <polygon points="0,12 328,12 366,130 0,130" fill="var(--accent)"/>
    <polygon points="0,0 314,0 352,116 0,116" fill="var(--ink-light)"/>
  </svg>
  <h1 class="holder-name">Marcus T Bellamy</h1>

  <ul class="contact-list">
    <li class="contact-item">
      <svg class="contact-icon" viewBox="0 0 24 24" aria-hidden="true"><path fill="var(--accent)" d="M6.6 2.5l2.6 4.3-2 1.6c.9 2.8 3.3 5.6 6.2 7l1.8-1.8 4.3 2.4-1.3 3.5C11 19 4.8 12.4 4.2 4.4z"/></svg>
      <span>(407)555-0186</span>
    </li>
    <li class="contact-item">
      <svg class="contact-icon" viewBox="0 0 24 24" aria-hidden="true"><circle cx="12" cy="12" r="4" fill="none" stroke="var(--accent)" stroke-width="2.6"/><path d="M16 8v5.5c0 2 3.5 2 3.5-1.5A7.5 7.5 0 1 0 15.5 19" fill="none" stroke="var(--accent)" stroke-width="2.6"/></svg>
      <span>mbellamy@wayfarenow.example</span>
    </li>
    <li class="contact-item">
      <svg class="contact-icon" viewBox="0 0 24 24" aria-hidden="true"><path fill="var(--accent)" d="M12 2a7 7 0 0 0-7 7c0 5 7 13 7 13s7-8 7-13a7 7 0 0 0-7-7zm0 4a3 3 0 1 1 0 6 3 3 0 0 1 0-6z"/></svg>
      <span>4812 Quillmore Ave #164<br>Orlando , FL 32804</span>
    </li>
    <li class="contact-item">
      <svg class="contact-icon" viewBox="0 0 24 24" aria-hidden="true"><g fill="none" stroke="var(--accent)" stroke-width="2"><circle cx="12" cy="12" r="9"/><ellipse cx="12" cy="12" rx="4" ry="9"/><path d="M3 12h18M5 7h14M5 17h14"/></g></svg>
      <span>www.wayfarenow.example</span>
    </li>
  </ul>
</section>

<section class="card card-back">
  <div class="brand"><span class="brand-dot"></span>wayfarenow</div>
  <p class="back-url">www.wayfarenow.example</p>
</section>

</body>
</html>
```